Design professional label for greener chemicals (cleaning and lubrication) brand

Design a b2b professional label that is based on the examples given.
Size: 135 x 200 mm, please use text of the label description doc (only the kaltro stainless steel polish example design document has the right text and size)
It should include:
1. Logo, can be fully changed except the shape of "KALTRO", colors and fonts of the rest can be customized
2. Focus should be on professional market, we would like to express the professionalism and high quality of the product
3. Focus should be on our brand name "KALTRO BRIGHTER COMPOUNDS"
4. Should include product name, product description, danger sentences, danger symbol, user instructions, image
5. Should include numbers that explain what the product does: 1. Prewash 2. Clean 3. Protect 4. Preserve and highlight number 2.

Target Market(s)

Professional cleaning companies, steel industry, food industry, pharmacy industry

Industry/Entity Type

Cleaning industry, steel industry, food industry, boat cleaning, car cleaning, professional lubrication

Font styles to use
Sans Serif

Requirements
Must have
• Professional look, clean look, image, focus on our brand name
Nice to have
• Numbers (see explanation), label divided in three parts (logo and product name and image in the middle as the highlight)

```html
<!DOCTYPE html>
<html lang="en">
<head>
<meta charset="utf-8">
<title>Kaltro Stainless Steel Polish – Label</title>
<link rel="stylesheet" href="https://fonts.googleapis.com/css2?family=Anton&family=Jost:wght@400;500&family=Montserrat:ital,wght@0,800;0,900;1,800&family=Oswald:wght@400;500&display=swap">
<style>
  :root{
    --bg:#3a3a3c;
    --green-dark:#0f4a3a;
    --green-deep:#0a3a2c;
    --green-mid:#1d6b52;
    --green-lime:#8dc63f;
    --green-brand:#6cb33f;
    --silver-1:#c9cbcd;
    --silver-2:#f4f5f6;
    --ink:#0f3f31;
    --white:#ffffff;
    --danger:#d7141a;
  }
  *{margin:0;padding:0;box-sizing:border-box}
  html,body{width:1200px;height:1200px;overflow:hidden;background:var(--bg)}
  .label{position:absolute;left:40px;top:222px;width:1120px;height:757px;overflow:hidden;font-family:"Oswald",sans-serif;color:var(--ink)}
  .label-art{position:absolute;inset:0}
  .abs{position:absolute}
  .brand-name{left:404px;top:40px;width:314px;text-align:center;font-family:"Montserrat",sans-serif;font-weight:900;font-size:66px;line-height:88px;color:var(--green-brand);letter-spacing:1px}
  .tagline-bar{left:0;top:407px;width:262px;height:33px;background:var(--green-lime);clip-path:polygon(0 0,100% 0,92% 100%,0 100%)}
  .tagline{left:20px;top:407px;line-height:33px;font-family:"Montserrat",sans-serif;font-style:italic;font-weight:800;font-size:16px;color:var(--white);letter-spacing:.3px}
  .use-heading{left:33px;top:455px;font-family:"Oswald",sans-serif;font-size:6.5px;font-weight:500;color:var(--ink)}
  .use-caption{top:558px;width:90px;text-align:center;font-family:"Oswald",sans-serif;font-weight:500;font-size:6.3px;line-height:8px;color:var(--ink);text-transform:uppercase}
  .product-kind{left:360px;top:420px;width:400px;line-height:40px;text-align:center;font-family:"Montserrat",sans-serif;font-weight:900;font-size:31px;letter-spacing:1.5px;color:var(--ink)}
  .product-claim{left:360px;top:605px;width:400px;text-align:center;font-family:"Oswald",sans-serif;font-weight:500;font-size:19px;letter-spacing:.2px;color:var(--ink)}
  .product-claim .dot{display:inline-block;width:11px;height:11px;border-radius:50%;background:var(--ink);margin:0 8px;vertical-align:1px}
  .info-panel{left:849px;top:22px;width:246px;height:264px;background:rgba(255,255,255,.55)}
  .info-text{left:855px;top:24px;width:238px;font-size:11.6px;line-height:16px;color:var(--ink)}
  .info-text p{margin-bottom:10px}
  .info-text ul{list-style:none;margin-top:16px}
  .info-text li{padding-left:5px;text-indent:-5px}
  .field{left:859px;width:230px;height:28px;border-bottom:1px solid var(--ink);font-family:"Jost",sans-serif;font-weight:500;font-size:12.5px;color:var(--ink)}
  .hazard-box{left:859px;top:452px;width:221px;height:147px;background:var(--white);border-radius:14px}
  .hazard-text{left:865px;top:546px;width:210px;font-family:"Jost",sans-serif;font-size:5.4px;line-height:7px;color:var(--danger)}
  .label-number{left:1024px;top:473px;width:160px;transform:rotate(90deg);font-family:"Jost",sans-serif;font-size:12px;color:var(--ink)}
  .company{left:34px;top:666px;font-family:"Jost",sans-serif;font-size:10px;line-height:12px;color:var(--white)}
  .contact{top:716px;font-family:"Jost",sans-serif;font-size:12px;color:var(--white);display:flex;align-items:center;gap:6px}
  .contact svg{width:13px;height:13px}
</style>
</head>
<body>
<div class="label">
  <svg class="label-art" viewBox="0 0 1120 757" width="1120" height="757">
    <defs>
      <linearGradient id="silver" x1="0" y1="0" x2="0" y2="1">
        <stop offset="0" stop-color="var(--silver-1)"/>
        <stop offset=".55" stop-color="var(--silver-1)"/>
        <stop offset=".62" stop-color="var(--silver-2)"/>
        <stop offset=".72" stop-color="var(--silver-1)"/>
        <stop offset=".86" stop-color="var(--silver-2)"/>
        <stop offset="1" stop-color="var(--silver-1)"/>
      </linearGradient>
      <linearGradient id="kitchen" x1="0" y1="0" x2="1" y2="1">
        <stop offset="0" stop-color="#b9bcbf"/>
        <stop offset=".45" stop-color="#8e9296"/>
        <stop offset=".75" stop-color="#c4c7ca"/>
        <stop offset="1" stop-color="#e9ecee"/>
      </linearGradient>
      <linearGradient id="polishFill" x1="0" y1="0" x2="0" y2="1">
        <stop offset="0" stop-color="var(--green-deep)"/>
        <stop offset=".5" stop-color="var(--green-mid)"/>
        <stop offset="1" stop-color="var(--green-deep)"/>
      </linearGradient>
    </defs>

    <rect class="label-base" width="1120" height="757" fill="url(#silver)"/>

    <path class="kitchen-photo" role="img" aria-label="Photo of a modern stainless steel kitchen with island and stool"
          d="M0 0H1120V296Q560 486 0 296Z" fill="url(#kitchen)"/>

    <path class="swoosh" d="M0 298Q560 488 1120 298" fill="none" stroke="var(--green-lime)" stroke-width="13"/>
    <path class="swoosh-soft" d="M0 310Q560 500 1120 310" fill="none" stroke="var(--green-lime)" stroke-opacity=".35" stroke-width="6"/>

    <circle class="badge" cx="331" cy="379" r="52" fill="var(--green-dark)"/>

    <g class="use-icons" fill="none" stroke="var(--green-dark)" stroke-width="3">
      <rect x="25" y="472" width="80" height="79" rx="14" role="img" aria-label="Icon: stainless steel kitchens"/>
      <rect x="120" y="472" width="79" height="79" rx="14" role="img" aria-label="Icon: boats"/>
      <rect x="215" y="472" width="79" height="79" rx="14" role="img" aria-label="Icon: industrial steel surfaces"/>
    </g>

    <text class="product-name" x="343" y="601" textLength="434" lengthAdjust="spacingAndGlyphs"
          font-family="Anton, sans-serif" font-size="148" fill="url(#polishFill)"
          stroke="var(--green-deep)" stroke-width="2">POLISH</text>

    <path class="footer-band-edge" d="M0 624Q560 698 1120 622V757H0Z" fill="var(--white)" fill-opacity=".6"/>
    <path class="footer-band" d="M0 630Q560 705 1120 628V757H0Z" fill="var(--green-dark)"/>

    <g class="hazard-symbols" transform="translate(967 496)">
      <g fill="var(--white)" stroke="var(--danger)" stroke-width="2.5">
        <rect x="-13" y="-13" width="26" height="26" transform="translate(0 -22) rotate(45)"/>
        <rect x="-13" y="-13" width="26" height="26" transform="translate(-22 0) rotate(45)"/>
        <rect x="-13" y="-13" width="26" height="26" transform="translate(22 0) rotate(45)"/>
        <rect x="-13" y="-13" width="26" height="26" transform="translate(0 22) rotate(45)"/>
      </g>
      <g fill="#111">
        <rect x="20.3" y="-9" width="3.4" height="12"/>
        <circle cx="22" cy="7" r="2"/>
      </g>
    </g>
  </svg>

  <div class="abs brand-name">KALTRO</div>

  <div class="abs tagline-bar"></div>
  <div class="abs tagline">BRIGHTER COMPOUNDS</div>

  <div class="abs use-heading">USE ON/FOR:</div>
  <div class="abs use-caption" style="left:20px">Stainless<br>steel kitchens</div>
  <div class="abs use-caption" style="left:115px">Boats</div>
  <div class="abs use-caption" style="left:210px">Industrial<br>steel surfaces</div>

  <div class="abs product-kind">STAINLESS STEEL</div>
  <div class="abs product-claim"><span class="dot"></span>RESTORE STEEL SURFACES HOLOGRAM FREE<span class="dot"></span></div>

  <div class="abs info-panel"></div>
  <div class="abs info-text">
    <p>Product description:<br>Lumarex is a mildly abrasive cleansing cream with preservative properties. For removing stubborn dirt, water stains and deposits on stainless steel with a hologram free finish. Lumarex is non-tox and safe to use.</p>
    <p>User instructions:</p>
    <ul>
      <li>- Shake before use.</li>
      <li>- Apply with a damp brush, sponge or pad.</li>
      <li>- Adjust rubbing pressure and duration to the persistence of the soiling.</li>
      <li>- Add water as needed while rubbing, rub in the direction of the structure.</li>
      <li>- Rinse with clean water.</li>
    </ul>
  </div>

  <div class="abs field" style="top:316px">Expiring dates:</div>
  <div class="abs field" style="top:362px">Batch number:</div>
  <div class="abs field" style="top:410px">Net volume:</div>

  <div class="abs hazard-box"></div>
  <div class="abs hazard-text">Danger: Causes severe skin burns and eye damage. Wear protective gloves, protective clothing, eye protection, face protection.<br>IF SWALLOWED: rinse mouth – DO NOT induce vomiting. Immediately call a POISON CENTER, a physician.<br>IF ON SKIN (or hair): Take off immediately all contaminated clothing.</div>

  <div class="abs label-number">Label number: 23092021</div>

  <div class="abs company">
    Company information:<br>
    Produced by Kaltro Laboratories Int. B.V.<br>
    Postbus 4821 - 5900 AB Venlo (NL)<br>
    Phone NL: +31 477 20 61 90<br>
    Kerkstraat 88 bus 14 – 3600 Genk (B)<br>
    Phone B: +32 89 41 07 50
  </div>

  <div class="abs contact" style="left:383px">
    <svg viewBox="0 0 14 14"><circle cx="7" cy="7" r="6.2" fill="none" stroke="#fff" stroke-width="1.1"/><rect x="3.6" y="4.6" width="6.8" height="4.8" fill="none" stroke="#fff" stroke-width=".9"/><path d="M3.6 4.8L7 7.5L10.4 4.8" fill="none" stroke="#fff" stroke-width=".9"/></svg>
    hello@kaltrochemicals.com
  </div>
  <div class="abs contact" style="left:570px">
    <svg viewBox="0 0 14 14" fill="none" stroke="#fff" stroke-width="1"><circle cx="7" cy="7" r="6.2"/><ellipse cx="7" cy="7" rx="2.7" ry="6.2"/><path d="M1 7H13M2 4H12M2 10H12"/></svg>
    www.kaltrochemicals.com
  </div>
</div>
</body>
</html>
```